Surgical Sales Presentation Folder

Presentation folder; three panel; custom cutouts; Six 8.5 x 11 full color sales sheets to be bound into presentation folder; 5 full color sales sheets, stepped, longest being 8.5 x 11.
We are Kelvar Surgical Group and we are a surgical company that supports physicians who wish to become surgeons. Our clients are Physicians. As such, the design needs to be very professional.
I have included a list of photos and a letter describing what we like about each photo. I have included the verbiage with page identifiers. If this makes scene, please feel free to add photos to the inside of the folder or I can provide you with examples that we think are similar to what we are looking for.
Updates
Target Market(s)
Doctors who want to be surgeons.
Industry/Entity Type
Sales
Requirements
Must have
- Presentation folder; three panel; custom cutouts; Six 8.5 x 11 full color sales sheets to be bound into presentation folder; 5 full color sales sheets, stepped, longest being 8.5 x 11.

```html
<!DOCTYPE html>
<html lang="en">
<head>
<meta charset="utf-8">
<title>Kelvar Surgical Group – Presentation Folder</title>
<link href="https://fonts.googleapis.com/css2?family=Russo+One&family=Roboto:wght@400;500&family=Oswald:wght@400&display=swap" rel="stylesheet">
<style>
  :root{
    --canvas:#d0d1d3;
    --heading:#2b2b2d;
    --brand-blue:#0aa9e6;
    --logo-blue:#1b6fae;
    --paper:#ffffff;
    --ink:#222222;
    --scrub-green:#1f5a4c;
    --scrub-light:#3f7f6c;
    --skin:#c8a58e;
    --insert-grey:#8e8f91;
  }
  *{margin:0;padding:0;box-sizing:border-box}
  html,body{width:1200px;height:2637px;overflow:hidden}
  body{background:var(--canvas);position:relative;font-family:"Roboto",sans-serif}
  .view-title{position:absolute;left:0;width:1200px;text-align:center;font-family:"Russo One",sans-serif;font-size:104px;line-height:1;color:var(--heading);letter-spacing:2px}
  .abs{position:absolute}
  .brand-name{font-family:"Roboto",sans-serif;font-weight:500;color:var(--logo-blue);white-space:nowrap;display:flex;align-items:center;gap:8px}
  .brand-dot{border-radius:50%;background:var(--logo-blue);flex:none}
  .brand-words{display:flex;flex-direction:column;align-items:flex-end;line-height:1}
  .front-logo{left:452px;top:478px;font-size:25px}
  .front-logo .brand-dot{width:26px;height:26px}
  .front-logo .brand-sub{font-size:16px;letter-spacing:1px;margin-top:3px}
  .inside-copy{left:401px;top:1490px;width:162px;font-family:"Oswald",sans-serif;font-size:8.6px;line-height:11.6px;color:var(--ink)}
  .back-page{left:361px;top:1891px;width:478px;height:680px;background:var(--paper);border:1px solid #b9b9b9}
  .back-band{left:166px;top:0;width:153px;height:437px;background:var(--brand-blue)}
  .back-photo{left:172px;width:132px;border:3px solid var(--paper)}
  .photo-eyes{top:47px;height:106px;background:linear-gradient(180deg,#dfe7ee,#c9b3a4 45%,#7fb4cf)}
  .photo-symbol{top:171px;height:100px;background:radial-gradient(circle at 50% 50%,#d8e6f5,#2b5c9a 70%)}
  .photo-tools{top:292px;height:111px;background:linear-gradient(135deg,#cfe6f4,#3f87bd 60%,#1d4f86)}
  .back-copy{left:90px;top:468px;width:298px;text-align:center;font-size:11.2px;line-height:14px;color:var(--ink)}
  .back-logo{left:0;width:476px;top:600px;justify-content:center;font-size:15px}
  .back-logo .brand-dot{width:14px;height:14px}
</style>
</head>
<body>

  <!-- FRONT -->
  <div class="view-title" style="top:42px">FRONT</div>
  <svg class="abs" style="left:327px;top:163px" width="530" height="707" viewBox="0 0 530 707">
    <rect width="530" height="707" fill="var(--brand-blue)"/>
    <path d="M0 0 H300 C445 160 445 550 300 707 H0 Z" fill="var(--paper)"/>
    <rect x="459" y="219" width="32" height="264" rx="16" fill="var(--paper)"/>
  </svg>
  <div class="abs brand-name front-logo">
    <span class="brand-dot"></span>
    <span class="brand-words"><span>KELVAR SURGICAL</span><span class="brand-sub">GROUP</span></span>
  </div>

  <!-- INSIDE -->
  <div class="view-title" style="top:905px">INSIDE</div>
  <svg class="abs" style="left:0;top:1030px" width="1200" height="690" viewBox="0 0 1200 690">
    <defs>
      <clipPath id="flap-clip"><ellipse cx="400" cy="345" rx="282" ry="340"/></clipPath>
      <clipPath id="pocket-clip"><rect x="612" y="6" width="435" height="678"/></clipPath>
    </defs>
    <rect x="612" y="6" width="435" height="678" fill="var(--brand-blue)"/>
    <g role="img" aria-label="Sales sheet insert tucked into the pocket">
      <rect x="744" y="38" width="105" height="92" fill="var(--insert-grey)"/>
      <rect x="762" y="58" width="87" height="28" fill="var(--paper)"/>
    </g>
    <text x="770" y="78" font-family="Roboto, sans-serif" font-weight="500" font-size="16" fill="var(--logo-blue)">KELV</text>
    <g clip-path="url(#pocket-clip)">
      <circle cx="790" cy="480" r="82" fill="#d9dcdf" role="img" aria-label="Blank CD in the pocket"/>
      <circle cx="790" cy="480" r="16" fill="var(--brand-blue)"/>
      <path d="M852 6 C760 160 705 360 735 684" fill="none" stroke="var(--paper)" stroke-width="5"/>
    </g>
    <ellipse cx="400" cy="345" rx="282" ry="340" fill="var(--paper)"/>
    <rect x="92" y="257" width="40" height="190" rx="18" fill="var(--paper)"/>
    <g clip-path="url(#flap-clip)">
      <rect x="174" y="46" width="380" height="242" fill="var(--skin)" role="img" aria-label="Surgeon in green scrub cap, seen from behind"/>
      <rect x="174" y="46" width="380" height="120" fill="var(--scrub-light)"/>
      <rect x="174" y="307" width="145" height="140" fill="var(--scrub-green)" role="img" aria-label="Close-up of green surgical gown"/>
      <rect x="330" y="307" width="224" height="140" fill="var(--scrub-light)" role="img" aria-label="Close-up of green surgical gown collar"/>
      <rect x="185" y="457" width="205" height="240" fill="var(--scrub-green)" role="img" aria-label="Back of green surgical gown"/>
    </g>
  </svg>
  <p class="abs inside-copy">Through the years, the high quality of patient care provided by physicians has remained constant. However, beset the needs of their medical practice many physicians find themselves needing to spend less time with a greater number of patients. Through the years, the high quality of patient care provided by physicians has remained constant. However, beset the needs of their medical practice many physicians find themselves needing to spend less time with a greater number of patients. They also commit a larger percentage of their income to the maintenance of their practice. They also commit a larger percentage of their income to the maintenance of</p>

  <!-- BACK -->
  <div class="view-title" style="top:1762px">BACK</div>
  <div class="abs back-page">
    <div class="abs back-band"></div>
    <div class="abs back-photo photo-eyes" role="img" aria-label="Surgeon wearing cap and mask"></div>
    <div class="abs back-photo photo-symbol" role="img" aria-label="Medical caduceus symbol in blue"></div>
    <div class="abs back-photo photo-tools" role="img" aria-label="Surgical instruments in blue light"></div>
    <p class="abs back-copy">Through the years, the high quality of patient care provided by physicians has remained constant. However, beset the needs of their medical practice many physicians find themselves needing to spend less time with a greater number of patients. They also commit a larger percentage of their income to the maintenance of their practice.</p>
    <div class="abs brand-name back-logo"><span class="brand-dot"></span>KELVAR SURGICAL GROUP</div>
  </div>

</body>
</html>
```